Business card for a "family office" company

Please provide professional looking business card designs, incorporating the attached logo and below details. Harrowmere Holdings Pty Ltd is a family office / financial investment company. We are looking for a modern, professional and contemporary card design.

Industry/Entity Type

Finance

Contact Information for Business Card

Name: Dean Mollick
Title: Director
Company: Harrowmere Holdings Pty Ltd
Email: harrowdean@quillnet.example
Mobile: 0462 735 418
Address: 4/312 Barnaby Parade, Marlowe Bay WA 6164, Australia

Requirements
Must have
• All details above and the logo. logo only on back side. incorporate colours of logo
Nice to have
• up to you
Should not have
• ?

```html
<!DOCTYPE html>
<html lang="en">
<head>
<meta charset="utf-8">
<title>Harrowmere Holdings – Business Card</title>
<link rel="stylesheet" href="https://fonts.googleapis.com/css2?family=Open+Sans:wght@400;600;700&display=swap">
<style>
  :root {
    --navy: #2c2a7c;
    --navy-deep: #1f1d5e;
    --navy-light: #3a3890;
    --paper: #ffffff;
    --paper-shade: #eeeeef;
    --ink: #1c1c22;
    --backdrop: #e4e2dc;
  }
  * { box-sizing: border-box; margin: 0; padding: 0; }
  html, body { width: 1200px; height: 800px; overflow: hidden; }
  body {
    background: var(--backdrop);
    font-family: "Open Sans", Arial, sans-serif;
    position: relative;
  }
  .card {
    position: absolute;
    width: 560px;
    height: 320px;
    border-radius: 3px;
    box-shadow: 0 10px 28px rgba(0,0,0,.22);
    overflow: hidden;
  }
  /* Back side */
  .card-back {
    left: 90px; top: 60px;
    background: radial-gradient(ellipse at 50% 30%, var(--navy-light) 0%, var(--navy) 55%, var(--navy-deep) 100%);
  }
  .card-back .texture {
    position: absolute; inset: 0;
    background: linear-gradient(180deg, rgba(255,255,255,0) 40%, rgba(255,255,255,.05) 100%);
  }
  .back-brand {
    position: absolute; left: 0; right: 0; top: 140px;
    display: flex; align-items: center; justify-content: center; gap: 14px;
    color: #fff; font-weight: 600; font-size: 34px; letter-spacing: 2px;
  }
  .back-brand .mark { width: 22px; height: 22px; background: #fff; }

  /* Front side */
  .card-front {
    left: 550px; top: 420px;
    background: linear-gradient(160deg, var(--paper) 50%, var(--paper-shade) 100%);
  }
  .card-front svg.rules { position: absolute; inset: 0; }
  .identity {
    position: absolute; left: 30px; top: 36px;
    padding-left: 14px; border-left: 8px solid var(--navy);
    color: var(--ink);
  }
  .identity .name { font-size: 24px; line-height: 1; }
  .identity .name strong { font-weight: 700; }
  .identity .role { font-size: 12px; margin-top: 3px; }

  .contacts {
    position: absolute; left: 30px; top: 186px;
    list-style: none; color: var(--ink); font-size: 13.5px;
  }
  .contacts li { display: flex; align-items: flex-start; gap: 14px; margin-bottom: 8px; line-height: 1.35; }
  .contacts svg { width: 14px; height: 14px; flex: none; margin-top: 2px; fill: var(--navy); }

  .front-brand {
    position: absolute; right: 28px; top: 116px;
    display: flex; align-items: center; gap: 10px;
    color: var(--navy); font-weight: 600; font-size: 19px; letter-spacing: 1px;
  }
  .front-brand .mark { width: 15px; height: 15px; background: var(--navy); }
  .website {
    position: absolute; right: 28px; top: 150px;
    color: var(--navy); font-size: 13px; line-height: 18px;
  }
</style>
</head>
<body>

  <section class="card card-back" aria-label="Card back">
    <div class="texture"></div>
    <div class="back-brand"><span class="mark"></span>Harrowmere Holdings</div>
  </section>

  <section class="card card-front" aria-label="Card front">
    <svg class="rules" viewBox="0 0 560 320" width="560" height="320">
      <path d="M0 92 H380 L392 80 H560" fill="none" stroke="var(--navy)" stroke-width="4"/>
      <line x1="0" y1="98" x2="380" y2="98" stroke="var(--navy)" stroke-width="1"/>
      <line x1="250" y1="168" x2="395" y2="168" stroke="var(--navy)" stroke-width="2"/>
      <line x1="0" y1="296" x2="560" y2="296" stroke="var(--navy)" stroke-width="2"/>
    </svg>

    <div class="identity">
      <p class="name">Dean <strong>Mollick</strong></p>
      <p class="role">Director</p>
    </div>

    <ul class="contacts">
      <li>
        <svg viewBox="0 0 16 16" aria-hidden="true"><path d="M1 3h14v10H1z M1 3l7 6 7-6" fill="var(--navy)" stroke="#fff" stroke-width="1"/></svg>
        harrowdean@quillnet.example
      </li>
      <li>
        <svg viewBox="0 0 16 16" aria-hidden="true"><path d="M4 0h8a1 1 0 0 1 1 1v14a1 1 0 0 1-1 1H4a1 1 0 0 1-1-1V1a1 1 0 0 1 1-1zm1 2v10h6V2z"/></svg>
        0462 735 418
      </li>
      <li>
        <svg viewBox="0 0 16 16" aria-hidden="true"><path d="M8 0a5.5 5.5 0 0 1 5.5 5.5C13.5 10 8 16 8 16S2.5 10 2.5 5.5A5.5 5.5 0 0 1 8 0zm0 3.5a2 2 0 1 0 0 4 2 2 0 0 0 0-4z"/></svg>
        <span>4/312 Barnaby Parade<br>Marlowe Bay WA 6164, Australia</span>
      </li>
    </ul>

    <div class="front-brand"><span class="mark"></span>Harrowmere Holdings</div>
    <p class="website">harrowmere.example</p>
  </section>

</body>
</html>
```